Restaurant Poster Design Project for A-Frame

I am after a poster, which will go on an outdoor A-Frame (A1 size - this size is to be confirmed) outlining our drink/happy hour/specials for our Mexican Restaurant and Bar.

Specific details are:

$4 Beer, Wine and Spirits
$5 Margaritas
everynight 5:30pm-7:30pm

I will supply logo, which needs to be incorporated (really small) into the poster, along with our address: 42 Birchwood Lane, Windsor - (Im not too sure if we should include our phone number or not ?? Please advise what you feel will look good etc

Happy for you to add a phrase or wording etc, as long as the specific details are included, above.

We also have an enclosed beer garden in the rear of the restaurant - Do you believe I should mention this?

I am really open to eye catching designs and ALL suggestions welcome please!
Updates

Please find attached of samples that I am sort of after: (please let me know if they cant be opened).

http://www.flyerwisp.com/blog/wp-content/uploads/2012/06/happyHourPoster-e1340372894746.gif

http://marnelvek.files.pagekiln.com/2012/10/profolio_0012.jpg?w=1169

http://3.cd.notequill.com/-NfNjpdG5w/T5pohPd0AhI/AAAAAAAADRs/CA7DPeI_PyU/s640/vintage_poster.jpg

http://www.quorvanhill.com/files/imagecache/Event/news/teaser/Lounge_Happy_Hour_Poster_-_Mar_2011_bilingual.jpg

http://www.tpelmors.com/dallas/images/happyhour_poster.jpg

http://cdn2-b.newsgarrow.com/sites/default/files/styles/large_lightbox/hash/9a/d1/9ad11350ba178511886fddcff7aaac8d.jpg?itok=wDl2vlfJ

http://www.platefinchly.com/imageservice/images/13/1313171414293_244/img_large_watermarked.jpg

Target Market(s)

18 YEARS OLD AND OVER

Industry/Entity Type

Restaurant

Requirements
Must have
• Address
Phone Number
Logo
Clear easy to read font, to be seen via cars + ppl walking down street
If images are included, to be clear and visable
Nice to have
• Images are possible
To mention a beer garden
Should not have
• Traditional Mexican Colourful 80's Theme

```html
<!DOCTYPE html>
<html lang="en">
<head>
<meta charset="utf-8">
<title>Happy Hour – Cantina Verde</title>
<link href="https://fonts.googleapis.com/css2?family=Quicksand:wght@700&display=swap" rel="stylesheet">
<style>
  :root {
    --ink: #111111;
    --paper: #ffffff;
    --frame: #9a9a9a;
    --zig-warm: #fbe9e4;
    --zig-cool: #e6eef8;
    --zig-gold: #fbf3dc;
  }
  * { box-sizing: border-box; margin: 0; padding: 0; }
  html, body { width: 866px; height: 1200px; overflow: hidden; background: var(--paper); }
  .poster {
    position: relative;
    width: 866px;
    height: 1200px;
    border: 2px solid var(--frame);
    font-family: 'Quicksand', sans-serif;
    font-weight: 700;
    color: var(--ink);
    text-transform: uppercase;
    overflow: hidden;
  }
  .backdrop {
    position: absolute;
    inset: 0;
    background: linear-gradient(180deg, var(--zig-warm) 0%, var(--zig-cool) 35%, var(--zig-gold) 65%, var(--zig-warm) 100%);
    opacity: 0.55;
  }
  .line {
    position: absolute;
    left: 0;
    width: 100%;
    text-align: center;
    line-height: 1;
    white-space: nowrap;
  }
  .headline { font-size: 208px; letter-spacing: -4px; transform: translateY(-50%) scaleY(1.3); }
  .headline--happy { top: 168px; }
  .headline--hour { top: 410px; }
  .offer--spirits { top: 595px; font-size: 47px; transform: translateY(-50%) scaleY(1.25); }
  .offer--margaritas { top: 718px; font-size: 82px; transform: translateY(-50%) scaleY(1.35); }
  .schedule--days { top: 847px; font-size: 70px; transform: translateY(-50%) scaleY(1.1); }
  .schedule--time { top: 926px; font-size: 92px; transform: translateY(-50%) scaleY(1.35); }
  .time-rule {
    position: absolute;
    top: 983px;
    left: 180px;
    width: 516px;
    height: 5px;
    background: var(--ink);
  }
  .address {
    position: absolute;
    left: 48px;
    top: 1085px;
    font-size: 32px;
    line-height: 1;
    transform: translateY(-50%);
    white-space: nowrap;
  }
  .brand {
    position: absolute;
    left: 606px;
    top: 1030px;
    width: 222px;
    height: 110px;
    display: flex;
    align-items: center;
    justify-content: center;
    gap: 10px;
    background: var(--paper);
  }
  .brand__dot { width: 18px; height: 18px; border-radius: 50%; background: var(--ink); flex: none; }
  .brand__name { font-size: 30px; line-height: 1.05; text-align: center; }
</style>
</head>
<body>
  <main class="poster">
    <div class="backdrop" role="img" aria-label="Faint multicoloured zigzag chevron pattern across the background"></div>

    <h1 class="line headline headline--happy">Happy</h1>
    <div class="line headline headline--hour">Hour!</div>

    <p class="line offer--spirits">$4 Beer, Wine and Spirits</p>
    <p class="line offer--margaritas">$5 Margaritas</p>

    <p class="line schedule--days">Everynight between</p>
    <p class="line schedule--time">5:30 - 7:30</p>
    <div class="time-rule"></div>

    <p class="address">42 Birchwood Lane, Windsor</p>
    <div class="brand">
      <span class="brand__dot"></span>
      <span class="brand__name">Cantina<br>Verde</span>
    </div>
  </main>
</body>
</html>
```